Business Card Design

We develop / design / build affordable housing throughout the state of Illinois.

Target Market(s)

non profit organizations and other developers / professionals in my industry

Industry/Entity Type

Business

Contact Information for Business Card

Birchstone Construction, LLC
General Contracting
Marisol K Thornbury, CEO
418 North Harlan W Ostrow Avenue, Suite 305
Larkfield, ST 00000
555-555-0147
mkt@buildbirchstone.com

```html
<!DOCTYPE html>
<html lang="en">
<head>
<meta charset="utf-8">
<title>Birchstone Construction – Business Card</title>
<link rel="stylesheet" href="https://fonts.googleapis.com/css2?family=Arimo:wght@700&family=Open+Sans:wght@300;400&display=swap">
<style>
  :root {
    --canvas-bg: #e9eaeb;
    --card-bg: #282828;
    --teal: #0a8f98;
    --teal-line: #1f7f86;
    --text-light: #f2f2f2;
  }
  * { margin: 0; padding: 0; box-sizing: border-box; }
  html, body {
    width: 1200px;
    height: 1200px;
    overflow: hidden;
    background: var(--canvas-bg);
  }
  .canvas {
    position: relative;
    width: 1200px;
    height: 1200px;
  }
  .card {
    position: absolute;
    top: 442px;
    width: 540px;
    height: 317px;
    background: var(--card-bg);
    box-shadow: 0 4px 14px rgba(0, 0, 0, 0.18);
    overflow: hidden;
  }
  .card--front { left: 40px; }
  .card--back { left: 620px; }

  .band {
    position: absolute;
    background: var(--teal);
  }
  .company {
    position: absolute;
    font-family: "Arimo", Arial, sans-serif;
    font-weight: 700;
    font-size: 19px;
    line-height: 23px;
    color: var(--teal);
    white-space: nowrap;
  }

  /* front */
  .card--front .band--tab { left: 0; top: 32px; width: 20px; height: 40px; }
  .card--front .band--bar { left: 284px; top: 35px; right: 0; height: 37px; }
  .card--front .company { left: 32px; top: 29px; }

  .person-name {
    position: absolute;
    left: 11px;
    top: 175px;
    font-family: "Open Sans", Arial, sans-serif;
    font-weight: 300;
    font-size: 17px;
    line-height: 22px;
    color: var(--teal);
  }
  .person-title {
    position: absolute;
    left: 11px;
    top: 199px;
    font-family: "Open Sans", Arial, sans-serif;
    font-weight: 400;
    font-size: 11px;
    line-height: 13px;
    color: var(--teal);
  }
  .divider {
    position: absolute;
    left: 11px;
    top: 215px;
    width: 517px;
    height: 1px;
    background: var(--teal-line);
  }
  .contact {
    position: absolute;
    left: 107px;
    top: 232px;
    font-family: "Open Sans", Arial, sans-serif;
    font-style: normal;
    font-weight: 300;
    font-size: 13px;
    line-height: 15px;
    color: var(--text-light);
    white-space: nowrap;
  }

  /* back */
  .card--back .band--bar { left: 0; top: 267px; width: 267px; height: 33px; }
  .card--back .band--tab { left: 530px; top: 265px; width: 10px; height: 38px; }
  .card--back .company { left: 276px; top: 261px; }
</style>
</head>
<body>
<main class="canvas">
  <section class="card card--front" aria-label="Business card front">
    <div class="band band--tab"></div>
    <div class="band band--bar"></div>
    <h1 class="company">Birchstone Construction<br>LLC General Contracting</h1>
    <p class="person-name">Marisol K Thornbury</p>
    <p class="person-title">CEO</p>
    <div class="divider"></div>
    <address class="contact">
      418 North Harlan W Ostrow Avenue, Suite 305 Larkfield<br>
      ST 00000 555-555-0147<br>
      mkt@buildbirchstone.com
    </address>
  </section>

  <section class="card card--back" aria-label="Business card back">
    <div class="band band--bar"></div>
    <p class="company">Birchstone Construction<br>LLC General Contracting</p>
    <div class="band band--tab"></div>
  </section>
</main>
</body>
</html>
```